Halvorsen Partners Business Card

Halvorsen Partners Civil Construction
Marcus Halvorsen
CEO
727-518-6094
Marcus@HalvorsenSiteworks.example
www.HalvorsenSiteworks.example
Site Development
Utility Construction
Excavation
40876 County Lane 19
Land O' Lakes, FL 34638

Target Market(s)

Construction and government

Industry/Entity Type

Business

Contact Information for Business Card

I want an unique design that make a statement

Number of Pages Required

1 page

Font styles to use

Colors

Designer to choose colors to be used in the design.

Requirements
Must have
• unique design, feel free to modify or change the color of my logo.
Nice to have
• extra design features like spot UV, foil accents, color edges, unique paper, or any thing that would make my card pop.
• I like the feel of the image that I attached

```html
<!DOCTYPE html>
<html lang="en">
<head>
<meta charset="utf-8">
<title>Halvorsen Partners Business Card</title>
<link href="https://fonts.googleapis.com/css2?family=Montserrat:wght@400;500;600&family=Oswald:wght@500&display=swap" rel="stylesheet">
<style>
  :root {
    --page-bg: #4a4a4a;
    --card-bg: #1c1c1d;
    --card-sheen: #2b2b2d;
    --ink: #f2f2f2;
    --ink-soft: #bdbdbd;
    --edge-gold: #c99a1e;
  }
  * { margin: 0; padding: 0; box-sizing: border-box; }
  html, body {
    width: 1200px; height: 864px; overflow: hidden;
    background: var(--page-bg);
    font-family: "Montserrat", sans-serif;
    color: var(--ink);
  }
  .card {
    position: absolute;
    width: 560px; height: 320px;
    background: radial-gradient(ellipse at 55% 25%, var(--card-sheen), var(--card-bg) 70%);
    border-bottom: 6px solid var(--edge-gold);
    box-shadow: 0 14px 30px rgba(0,0,0,.45);
  }
  .card--front { left: 70px; top: 70px; }
  .card--back { left: 570px; top: 474px; }

  /* front */
  .brand {
    position: absolute; left: 90px; top: 96px;
    display: flex; align-items: center; gap: 16px;
  }
  .brand__square { width: 44px; height: 44px; background: var(--ink); }
  .brand__name {
    font-weight: 600; color: var(--ink); text-transform: uppercase;
    line-height: 1.25;
  }
  .brand__name .line1 { display: block; font-size: 24px; letter-spacing: .02em; }
  .brand__name .line2 { display: block; font-size: 13px; letter-spacing: .36em; }
  .services {
    position: absolute; left: 0; right: 0; bottom: 34px;
    text-align: center; font-size: 13px; font-weight: 500; letter-spacing: .03em;
  }
  .services .dot { margin: 0 10px; }

  /* back */
  .person {
    position: absolute; left: 70px; top: 108px; width: 200px;
    text-align: right;
  }
  .person__name {
    font-family: "Oswald", sans-serif; font-weight: 500;
    font-size: 30px; text-transform: uppercase; letter-spacing: .01em; line-height: 1.1;
  }
  .person__title { font-size: 13px; color: var(--ink); margin-top: 2px; }
  .divider {
    position: absolute; left: 286px; top: 96px; width: 1px; height: 80px; background: var(--ink-soft);
  }
  .contacts {
    position: absolute; left: 302px; top: 96px; list-style: none;
    font-size: 12px; line-height: 20px;
  }
  .contacts li { display: flex; align-items: center; gap: 7px; white-space: nowrap; }
  .contacts svg { width: 11px; height: 11px; fill: var(--ink); flex: none; }
  .address {
    position: absolute; left: 0; right: 0; bottom: 38px;
    text-align: center; font-size: 14px; font-weight: 500;
  }
</style>
</head>
<body>
  <section class="card card--front" aria-label="Card front">
    <div class="brand">
      <span class="brand__square"></span>
      <span class="brand__name">
        <span class="line1">Halvorsen Partners</span>
        <span class="line2">Civil Construction</span>
      </span>
    </div>
    <p class="services">Site Development<span class="dot">•</span>Utility Construction<span class="dot">•</span>Excavation</p>
  </section>

  <section class="card card--back" aria-label="Card back">
    <div class="person">
      <h1 class="person__name">Marcus Halvorsen</h1>
      <p class="person__title">CEO</p>
    </div>
    <span class="divider"></span>
    <ul class="contacts">
      <li><svg viewBox="0 0 24 24"><path d="M6.6 10.8a15.1 15.1 0 0 0 6.6 6.6l2.2-2.2c.3-.3.7-.4 1-.2 1.1.4 2.3.6 3.6.6.6 0 1 .4 1 1V20c0 .6-.4 1-1 1A17 17 0 0 1 3 4c0-.6.4-1 1-1h3.5c.6 0 1 .4 1 1 0 1.3.2 2.5.6 3.6.1.3 0 .7-.2 1z"/></svg>727-518-6094</li>
      <li><svg viewBox="0 0 24 24"><path d="M7 1h10a2 2 0 0 1 2 2v18a2 2 0 0 1-2 2H7a2 2 0 0 1-2-2V3a2 2 0 0 1 2-2zm0 3v15h10V4z"/></svg>000-000-0000</li>
      <li><svg viewBox="0 0 24 24"><path d="M2 5h20v14H2zm2 2v.5l8 5 8-5V7l-8 5z"/></svg>Marcus@HalvorsenSiteworks.example</li>
      <li><svg viewBox="0 0 24 24"><path d="M12 2a10 10 0 1 0 0 20 10 10 0 0 0 0-20zm1 2.1c1.5.6 2.6 3.1 2.9 6.9H13zm-2 0V11H8.1c.3-3.8 1.4-6.3 2.9-6.9zM4.1 13H6c.1 2.4.6 4.5 1.4 5.9A8 8 0 0 1 4.1 13zM4.1 11a8 8 0 0 1 3.3-5.9C6.6 6.5 6.1 8.6 6 11zm4 2H11v6.9c-1.5-.6-2.6-3.1-2.9-6.9zm4.9 6.9V13h2.9c-.3 3.8-1.4 6.3-2.9 6.9zm3.6-1A14 14 0 0 0 18 13h1.9a8 8 0 0 1-3.3 5.9zM18 11a14 14 0 0 0-1.4-5.9A8 8 0 0 1 19.9 11z"/></svg>www.HalvorsenSiteworks.example</li>
    </ul>
    <p class="address">Halvorsen Partners : 40876 County Lane 19, Land O' Lakes, FL 34638</p>
  </section>
</body>
</html>
```